Card design for orthopaedic surgeons working as The Brindlewood Orthopaedic Centre

Business cards, letterhead

Colors

Designer to choose colors to be used in the design.

Requirements
Must have
• Late addition.
• Cards letterhead must have logos of
• Corvane Federated Institute of Surgeons
• Meridale Orthopaedic Society
Nice to have
• Back of card to have space for appointment time to be added by hand and some blank space for writing incidental other notes.

```html
<!DOCTYPE html>
<html lang="en">
<head>
<meta charset="utf-8">
<title>The Brindlewood Orthopaedic Centre – Business Card</title>
<link rel="stylesheet" href="https://fonts.googleapis.com/css2?family=Source+Sans+3:wght@400;600;700&display=swap">
<style>
  :root {
    --backdrop: #2b2b2b;
    --card-white: #ffffff;
    --sky: #2fadf5;
    --sky-text: #2aa4ee;
    --navy: #0f2a44;
    --ink: #4a4a4a;
    --rule: #8d8d8d;
    --badge: #d6ecfa;
    --write-line: rgba(255, 255, 255, 0.7);
  }
  * { margin: 0; padding: 0; box-sizing: border-box; }
  html, body {
    width: 1200px; height: 960px; overflow: hidden;
    background: var(--backdrop);
    font-family: "Source Sans 3", "Helvetica Neue", Arial, sans-serif;
  }
  .stage { position: relative; width: 1200px; height: 960px; }

  .card {
    position: absolute; left: 262px; width: 678px; height: 386px;
    border-radius: 22px; overflow: hidden;
  }
  .card--front { top: 62px; background: var(--card-white); }
  .card--back { top: 512px; background: var(--sky); }

  .brand-name {
    position: absolute; white-space: nowrap;
    font-weight: 400; letter-spacing: -0.4px;
  }
  .card--front .brand-name {
    left: 56px; top: 192px; font-size: 19.5px; color: var(--sky-text);
  }
  .card--back .brand-name {
    left: 0; right: 0; text-align: center; top: 192px;
    font-size: 24px; color: var(--card-white);
  }

  .society-badges {
    position: absolute; left: 150px; top: 238px;
    display: flex; gap: 18px;
  }
  .society-badge {
    width: 40px; height: 40px; border-radius: 50%;
    background: var(--badge);
  }

  .divider {
    position: absolute; left: 363px; top: 80px;
    width: 1.5px; height: 235px; background: var(--rule);
  }

  .contact { position: absolute; left: 392px; top: 88px; }
  .contact__name { font-size: 21px; font-weight: 600; color: var(--sky-text); line-height: 1.1; }
  .contact__title { font-size: 15px; font-weight: 700; color: var(--navy); line-height: 1.3; margin-bottom: 14px; }
  .contact__address { font-size: 15px; color: var(--ink); line-height: 21px; margin-bottom: 10px; }
  .contact__list { list-style: none; }
  .contact__list li {
    display: flex; align-items: center; gap: 9px;
    font-size: 15px; color: var(--ink); line-height: 20.4px;
  }
  .contact__list svg { width: 15px; height: 15px; fill: var(--sky-text); flex: none; }

  .wave { position: absolute; left: 0; bottom: 0; width: 678px; height: 386px; }

  .appointment-lines {
    position: absolute; left: 159px; top: 268px; width: 360px;
  }
  .appointment-lines span {
    display: block; height: 1px; background: var(--write-line);
    margin-bottom: 30px;
  }
</style>
</head>
<body>
<main class="stage">

  <section class="card card--front" aria-label="Business card front">
    <div class="brand-name">The Brindlewood Orthopaedic Centre</div>
    <div class="society-badges">
      <div class="society-badge" role="img" aria-label="Corvane Federated Institute of Surgeons membership badge"></div>
      <div class="society-badge" role="img" aria-label="Meridale Orthopaedic Society membership badge"></div>
    </div>
    <div class="divider"></div>

    <div class="contact">
      <div class="contact__name">Owen Hartley</div>
      <div class="contact__title">President</div>
      <div class="contact__address">2716 Ashcombe Lane<br>Larkfield, NY 11940</div>
      <ul class="contact__list">
        <li>
          <svg viewBox="0 0 16 16" aria-hidden="true"><path d="M2 6c0-2 2.5-3.5 6-3.5S14 4 14 6v1h-3V5.8C10 5.4 9 5.3 8 5.3s-2 .1-3 .5V7H2z"/><path d="M4 8h8l1.5 5.5h-11z"/></svg>
          (555) 2841-7730
        </li>
        <li>
          <svg viewBox="0 0 16 16" aria-hidden="true"><path d="M5 1h6a1 1 0 0 1 1 1v12a1 1 0 0 1-1 1H5a1 1 0 0 1-1-1V2a1 1 0 0 1 1-1zm.5 2v9h5V3z"/></svg>
          (555) 6193-4028
        </li>
        <li>
          <svg viewBox="0 0 16 16" aria-hidden="true"><path d="M4 1h6l2 2v4H4z"/><path d="M2 8h12v6H2zm2 2v1h2v-1zm4 0v1h2v-1z"/></svg>
          (555) 3907-1164
        </li>
        <li>
          <svg viewBox="0 0 16 16" aria-hidden="true"><path d="M1 4h14v1L8 9.5 1 5z"/><path d="M1 6.5l7 4.5 7-4.5V12H1z"/></svg>
          info@brindlewoodortho.com
        </li>
        <li>
          <svg viewBox="0 0 16 16" aria-hidden="true"><circle cx="8" cy="8" r="6.5"/><path d="M5 5c1 0 2 1 1.5 2S7 9 8 9.5 7.5 12 7 13" stroke="#fff" stroke-width="1.2" fill="none"/></svg>
          brindlewoodortho.com
        </li>
      </ul>
    </div>

    <svg class="wave" viewBox="0 0 678 386" aria-hidden="true">
      <path fill="var(--sky)" d="M0,372 C180,362 400,378 540,362 C610,354 650,335 678,312 L678,386 L0,386 Z"/>
      <path fill="var(--navy)" d="M6,366 C120,336 320,344 480,352 C570,356 630,334 668,312 C630,342 570,362 470,366 C320,370 150,356 6,370 Z"/>
    </svg>
  </section>

  <section class="card card--back" aria-label="Business card back">
    <div class="brand-name">The Brindlewood Orthopaedic Centre</div>
    <div class="appointment-lines" aria-label="Space to write appointment time and notes">
      <span></span>
      <span></span>
      <span></span>
    </div>
  </section>

</main>
</body>
</html>
```